We need a flyer where we promote a workshop to our members of the jewish community www.qvb-gemeinde.example . The workshop is calles "guidance in ten seasons presented by QVB. We would like to see a flyer with the below text is used and also some pictures (attached). The flyer should come over as cool, fresh, innovative for a younger crowd so called young professionals (age 28-35).
TITLE.
"Guidance in Ten Seasons.
SUBTITLE.
Your systematic self-coaching roadmap to power and impact—and your future.”
TEXT.
Dr. Martin K. Halvorsen is the CEO Emeritus of Alpine Advisory Partners—he made an exit in 2013. He is the award-winning author of 8 books, including "Plan-Into-Motion," "Speak or Falter" and "The Cantor and the Chairman.”
For the past 20 years he has taught leadership at Harwick University in New York and at BKU (Lindenberg University) to prepare future CEOs and other leaders in business, government , nonprofits and the military.
Now, in a process exclusively designed for QVB’s next generation of emerging leaders, Martin unpacks his leadership secrets in 3 action-packed labs—reduced to the max:
Lab 1. Guidance in Ten Seasons: The Summit Guide Triangle®. Self-Assessment. Self-Leadership: “The Lantern.” 5-Year Vision. 100-Day Catalytic Project.
Lab 2. Leading Through Language. Relationship: Building Trust. Plan-Into-Motion. Cockpit.
Lab 3. Debrief and Scale-Up. Sustainability. Action Tools.
Do you want to build your own future and a life you love? Do you want to jump-start that future and life over 100 days while learning a toolbox of leadership skills, networking with like-minded people—and even get some pizza? Then join us.
Target Market(s)
young professionals age 28-35

```html
<!DOCTYPE html>
<html lang="en">
<head>
<meta charset="utf-8">
<title>Guidance in Ten Seasons – QVB</title>
<link rel="stylesheet" href="https://fonts.googleapis.com/css2?family=Merriweather:wght@300;400;900&family=Barlow:wght@400;700&display=swap">
<style>
  :root {
    --page-grey: #dcdddc;
    --sky-mint: #c6eee8;
    --road-mint: #69d8c8;
    --signal-red: #e8402a;
    --white: #ffffff;
    --ink: #2b2b2b;
    --logo-grey: #3a3a3a;
    --serif: "Merriweather", Georgia, serif;
    --sans: "Barlow", Arial, sans-serif;
  }
  * { margin: 0; padding: 0; box-sizing: border-box; }
  html, body { width: 959px; height: 1200px; overflow: hidden; background: var(--page-grey); }
  .flyer {
    position: absolute; left: 66px; top: 66px; width: 827px; height: 1069px;
    background: var(--road-mint); overflow: hidden;
  }
  .backdrop { position: absolute; left: 0; top: 0; width: 827px; height: 1069px; }
  .title {
    position: absolute; left: 0; width: 827px; text-align: center; color: var(--white);
    font-family: var(--serif); white-space: nowrap;
  }
  .title-main { top: 90px; font-size: 76px; font-weight: 900; line-height: 1.2; }
  .title-sub { top: 170px; font-size: 62px; font-weight: 300; line-height: 1.2; }
  .subtitle { top: 246px; font-size: 27px; font-weight: 300; line-height: 42px; }
  .subtitle strong { font-weight: 900; }
  .portrait {
    position: absolute; left: 262px; top: 489px; width: 83px; height: 86px;
    border: 2px solid var(--signal-red);
    background: linear-gradient(160deg, #b9c8d2, #6d7780);
  }
  .bio { position: absolute; font-family: var(--sans); color: var(--ink); }
  .bio-intro { left: 360px; top: 489px; width: 212px; font-size: 11.3px; line-height: 13.6px; }
  .bio-intro strong { font-weight: 700; }
  .bio-teaching { left: 263px; top: 585px; width: 310px; font-size: 13.4px; line-height: 16.4px; }
  .invite-band {
    position: absolute; left: 88px; top: 694px; width: 654px; height: 84px;
    background: var(--signal-red); color: var(--white);
    font-family: var(--sans); font-weight: 700; font-size: 19.5px; line-height: 27.5px;
    padding: 1px 0 0 10px; white-space: nowrap;
  }
  .stage-photo {
    position: absolute; left: 88px; top: 793px; width: 317px; height: 176px;
    background: radial-gradient(ellipse at 55% 30%, #3b3f66 0%, #14173a 45%, #1c2fa0 100%);
  }
  .labs { position: absolute; left: 447px; top: 796px; width: 300px; font-family: var(--sans); color: var(--ink); font-size: 13.4px; line-height: 16.4px; }
  .lab { display: flex; margin-bottom: 12.5px; }
  .lab-label { width: 49px; flex: none; font-weight: 700; }
  .lab-text { width: 236px; }
  .footer-band {
    position: absolute; left: 0; top: 985px; width: 827px; height: 70px; background: var(--white);
  }
  .footer-copy {
    position: absolute; left: 45px; top: 16px;
    font-family: var(--sans); font-size: 12.6px; line-height: 15px; color: var(--ink); white-space: nowrap;
  }
  .footer-logo {
    position: absolute; left: 712px; top: 2px; width: 80px;
    font-family: var(--sans); font-weight: 700; font-size: 42px; line-height: 1.1; color: var(--logo-grey);
    text-align: center;
  }
  .footer-url {
    position: absolute; right: 42px; top: 52px;
    font-family: var(--sans); font-size: 12px; line-height: 1; color: var(--ink); white-space: nowrap;
  }
</style>
</head>
<body>
<main class="flyer">
  <svg class="backdrop" viewBox="0 0 827 1069">
    <defs>
      <clipPath id="sun-clip"><ellipse cx="413" cy="268" rx="325" ry="325"/></clipPath>
      <linearGradient id="skyline-tone" x1="0" y1="0" x2="0" y2="1">
        <stop offset="0" stop-color="#e8402a"/>
        <stop offset="1" stop-color="#c6eee8"/>
      </linearGradient>
    </defs>
    <rect x="0" y="0" width="827" height="1069" fill="var(--sky-mint)" aria-hidden="true"/>
    <ellipse cx="413" cy="268" rx="325" ry="325" fill="var(--signal-red)" aria-hidden="true"/>
    <g role="img" aria-label="Stylised city skyline silhouette rising above the road">
      <rect x="0" y="332" width="827" height="130" fill="url(#skyline-tone)" clip-path="url(#sun-clip)"/>
    </g>
    <g aria-hidden="true">
      <polygon points="260,450 580,450 827,648 827,1069 0,1069 0,641" fill="var(--road-mint)"/>
      <polygon points="284,450 297,450 0,728 0,703" fill="var(--white)"/>
      <polygon points="547,450 534,450 827,720 827,703" fill="var(--white)"/>
    </g>
  </svg>

  <h1 class="title title-main">GUIDANCE</h1>
  <p class="title title-sub">IN TEN SEASONS</p>
  <p class="title subtitle">Your systematic self-coaching roadmap to<br><strong>power and impact—and your future.</strong></p>

  <div class="portrait" role="img" aria-label="Portrait photo of Dr. Martin K. Halvorsen"></div>
  <p class="bio bio-intro">Dr. Martin K. Halvorsen is the CEO Emeritus of Alpine Advisory Partners—he made an exit in 2013. He is the award-winning author of 8 books, including <strong>"Plan-Into-Motion," "Speak or Falter"</strong> and <strong>“The Cantor and the Chairman.”</strong></p>
  <p class="bio bio-teaching">For the past 20 years he has taught leadership at Harwick University in New York and at BKU (Lindenberg University) to prepare future CEOs and other leaders in business, government , nonprofits and the military.</p>

  <p class="invite-band">Now, in a process exclusively designed for QVB’s next generation<br>of emerging leaders, Martin unpacks his leadership secrets in<br>3 action-packed labs—reduced to the max:</p>

  <div class="stage-photo" role="img" aria-label="Photo of a speaker on stage in front of a large audience"></div>

  <section class="labs">
    <div class="lab"><span class="lab-label">LAB 1.</span><span class="lab-text">Guidance in Ten Seasons: The Summit Guide Triangle®. Self-Assessment. Self-Leadership: “The Lantern.” 5-Year Vision. 100-Day Catalytic Project.</span></div>
    <div class="lab"><span class="lab-label">LAB 2.</span><span class="lab-text">Leading Through Language. Relationship: Building Trust. Plan-Into-Motion. Cockpit.</span></div>
    <div class="lab"><span class="lab-label">LAB 3.</span><span class="lab-text">Debrief and Scale-Up. Sustainability. Action Tools.</span></div>
  </section>

  <footer class="footer-band">
    <p class="footer-copy">Do you want to build your own future and a life you love? Do you want to jump-start that future and life over 100 days while<br>learning a toolbox of leadership skills, networking with like-minded people—and even get some pizza? Then join us.</p>
    <div class="footer-logo">QVB</div>
    <div class="footer-url">www.qvb-gemeinde.example</div>
  </footer>
</main>
</body>
</html>
```